Ridgely Forge business card for handing simple contact information and generating service awareness

Utilizing the attached logo(s), generate a professional, but approachable, card conveying a sense of capability and integrity. Please only use one logo of the four attached; the different colors are all acceptable, but preference will be given to a design integrating a teal/turquoise logo,

I do not know where to put in the contact information or details?

Target Market(s)

Agriculture, Farming, Timber, Forestry, Construction, Crane Service

Industry/Entity Type

Contact Information for Business Card

Name, Phone Number, email address

Colors

Designer to choose colors to be used in the design.

Requirements
Nice to have
• It would be great to have either a mountain or one of the attached cranes as a backdrop on the rear of the card. Simple watermarks and/or Debossing is also great

```html
<!DOCTYPE html>
<html lang="en">
<head>
<meta charset="utf-8">
<title>Ridgely Forge – Business Card</title>
<link href="https://fonts.googleapis.com/css2?family=Poppins:wght@400;500;700&display=swap" rel="stylesheet">
<style>
  :root {
    --teal: #2b6b5e;
    --teal-soft: #3b7e70;
    --ink: #1e1e1e;
    --paper: #ffffff;
    --rule: #c9c9d2;
    --stage: #2e2e2e;
  }
  * { box-sizing: border-box; margin: 0; padding: 0; }
  html, body { width: 1200px; height: 866px; overflow: hidden; }
  body {
    background: var(--stage);
    font-family: "Poppins", sans-serif;
    display: flex;
    align-items: center;
    justify-content: center;
    gap: 40px;
  }
  .card {
    position: relative;
    width: 540px;
    height: 309px;
    overflow: hidden;
    border-radius: 3px;
    box-shadow: 0 12px 28px rgba(0,0,0,.45);
  }
  /* Front */
  .card-front { background: var(--paper); color: var(--ink); }
  .front-backdrop {
    position: absolute; left: 60px; top: -20px;
    width: 240px; height: 300px; border-radius: 50%;
    background: radial-gradient(circle at 50% 40%, rgba(0,0,0,.06), rgba(0,0,0,.02) 60%, transparent 72%);
  }
  .contact { position: absolute; left: 34px; top: 44px; width: 250px; }
  .contact-name {
    font-weight: 700; color: var(--teal); font-size: 19px; letter-spacing: 1.5px;
    text-transform: uppercase; line-height: 1.1;
  }
  .contact-role { font-size: 14px; margin-top: 2px; }
  .contact-rule { height: 1px; background: var(--rule); margin: 10px 0 8px; }
  .contact-line { display: flex; align-items: center; gap: 8px; font-size: 14px; line-height: 1.55; }
  .contact-line svg { width: 13px; height: 13px; fill: var(--teal); flex: none; }
  .brand {
    position: absolute; right: 38px; top: 112px;
    display: flex; align-items: center; gap: 10px;
  }
  .brand-dot { width: 22px; height: 22px; border-radius: 50%; background: var(--teal); }
  .brand-name { font-weight: 700; font-size: 26px; color: var(--teal); text-transform: uppercase; letter-spacing: 1px; }
  .address {
    position: absolute; right: 40px; top: 192px; width: 210px;
    font-size: 13px; line-height: 1.45; text-align: left;
    border-top: 1px solid var(--rule); padding-top: 8px;
  }
  .front-band { position: absolute; left: 0; bottom: 0; width: 540px; height: 70px; }
  .website {
    position: absolute; right: 40px; bottom: 10px;
    color: var(--paper); font-size: 14px; letter-spacing: .5px;
  }
  /* Back */
  .card-back { background: var(--teal); }
  .back-backdrop {
    position: absolute; inset: 0;
    background: radial-gradient(ellipse at 40% 55%, var(--teal-soft), var(--teal) 65%);
  }
  .back-brand {
    position: absolute; inset: 0;
    display: flex; align-items: center; justify-content: center; gap: 12px;
  }
  .back-brand .brand-dot { background: var(--paper); width: 26px; height: 26px; }
  .back-brand .brand-name { color: var(--paper); font-size: 32px; }
</style>
</head>
<body>
  <section class="card card-front" aria-label="Card front">
    <div class="front-backdrop" role="img" aria-label="Faint mountain and forest watermark"></div>

    <div class="contact">
      <p class="contact-name">Daniel Harrow</p>
      <p class="contact-role">Managing Director</p>
      <div class="contact-rule"></div>
      <p class="contact-line">
        <svg viewBox="0 0 24 24" aria-hidden="true"><path d="M6.6 10.8a15 15 0 0 0 6.6 6.6l2.2-2.2a1 1 0 0 1 1-.25 11.4 11.4 0 0 0 3.6.57 1 1 0 0 1 1 1V20a1 1 0 0 1-1 1A17 17 0 0 1 3 4a1 1 0 0 1 1-1h3.5a1 1 0 0 1 1 1c0 1.25.2 2.45.57 3.6a1 1 0 0 1-.25 1z"/></svg>
        044-555 018 274
      </p>
      <p class="contact-line">
        <svg viewBox="0 0 24 24" aria-hidden="true"><path d="M2 5h20v14H2zm2 2v.5l8 5 8-5V7l-8 5z"/></svg>
        hello@ridgelyforge.net
      </p>
    </div>

    <div class="brand">
      <span class="brand-dot"></span>
      <span class="brand-name">Ridgely Forge</span>
    </div>

    <p class="address">421, Address line goes here<br>45452, Country Name</p>

    <svg class="front-band" viewBox="0 0 540 70" preserveAspectRatio="none" aria-hidden="true">
      <path d="M0 0 L0 8 L200 70 L540 70 L540 34 L250 34 C225 34 225 22 200 22 L60 22 Z" fill="var(--teal)"/>
      <path d="M0 0 L0 3 L210 68 L540 68" fill="none" stroke="var(--paper)" stroke-width="2"/>
    </svg>
    <p class="website">www.ridgelyforge.net</p>
  </section>

  <section class="card card-back" aria-label="Card back">
    <div class="back-backdrop" role="img" aria-label="Faint forest and mountain backdrop in teal tones"></div>
    <div class="back-brand">
      <span class="brand-dot"></span>
      <span class="brand-name">Ridgely Forge</span>
    </div>
  </section>
</body>
</html>
```